Gridwell Review Word Press Website Home Page, Form and Search Results Page

We are a website called "Gridwell Review" (www.GridwellReview.com) that provides Audit Tests descriptions for Technology Auditors to use. The website is under construction, however I have a test website to give you a better idea: www.pinecrestledger.org. I already have a logo and some icons that you'll be able to see at www.pinecrestledger.org.

I'm looking for a WebPress design I can give to my web programmer to implement on HostKestrel.

The central purpose of the website is to provide a place for auditors to find technology audit tests and for experienced auditors to add audit tests to the existing catalog of tests.

I'd like the website to be the gold standard in Technology Audit Tests so I will encourage auditors to edit the catalog of tests as well as submit new tests.

The Form to Add or Edit Audit Tests must include the following fields:
Field 1: Technology Type (i.e. Mainframe, Database, Network ...)
Field 2: Risk Description (i.e. Cyber Security Attack, Service Outage...)
Field 3: Control Description (i.e. Remove Leavers Access, Backup Data...)
Field 4: Audit Test (i.e. Check Leavers list with Access List, Check Backups can be Restored)
Field 5: Test Author Name (i.e. name of person that added the test)

Each audit test in the catalog will have information in the 5 fields above - this will give auditors what they need to know to perform an audit.Typically each audit test is displayed as a row in a table. For each technology type (i.e. Mainframe) there can be up to 30-40 tests. Together these tests form what's called an Audit Program (brovix will give you more info if you search for it).

I would like the Search results to also display the 5 fields above. For example if someone searches for "Backup" or "Mainframe" then the search result will show the 5 fields for each audit test relevant to "Backup" in a table format. I will limited the amount of text that can be added to each field so it can be displayed in a table on the web page.

The customer base is Technology Auditors and the website a place to them to find information about how to audit. Its important the website design looks modern, hi-tech and simple to use.

The visitors will come to the website typically audit cyber security, cloud computing, mainframes, payment systems etc hence it needs a high-tech feel.

As an example, a typically customer will be some that has been asked to audit a technology but has not done it before so they will come to the website to look for audit tests. The other type of customer will be someone that has just finished an audit and wants to share their tests that describes how they audited the technology.

It's important the website looks professional and gives a sense of trust as well as giving sense of high-tech, modern leading edge thinking.

In summary the website provides 4 things:
(1) An auditor can browse for audit tests by technology type (mainframe, database etc)
(2) Search for a test based on a criteria like "Cyber Security".
(3) Add/Submit an audit test or edit an existing test.
(4) Access other relevant auditor resources ( links and publications etc).

Target Market(s)

Professional Auditors that want to find information to help them in their day-to-day job.

Industry/Entity Type

Auditing

Logo Text

Gridwell Review

Number of Pages Required

3 page

Font styles to use
Sans Serif

Requirements
Must have
• A Word Press Theme I can pass to my web programmer.
• I need 3 pages designed:
• (1) A Home Page
• (2) A Form to Submit Audit Tests (see 5 fields above in project description)
• (3) A Search Results Page that lists the results from Search (see 5 fields in project description)
• The Home should list a sample of the audit test in two ways:
• (1) include a league table on the home page with the top 10 most popular audit tests showing the author, test title, technology types, and risk title.
• (2) A selection of the icons in a square or regular pattern, similar to a list of products. These will essentially be feature audit tests. Once a visitor click the icon they will be taken through to a table that will list all the audit tests relevant to that feature technology category i.e. cyber, resilience, mainframe etc.
• The website must have a Modern, Hi-Tech Design that is simple to use.
• I like the modern colors in website slider image on www.pinecrestledger.org
Nice to have
• Change color of icons (attached) to match the Logo and Slider image (both attached) as the orange and blue icons not match the logo.
Should not have
• The website will not have a Cart
• The website design must not be too busy or complicated.

```html
<!DOCTYPE html>
<html lang="en">
<head>
<meta charset="utf-8">
<title>Gridwell Review — Home</title>
<link href="https://fonts.googleapis.com/css2?family=Barlow:wght@300;400;500;600&display=swap" rel="stylesheet">
<style>
:root{
  --teal:#1aa3b5;
  --teal-dark:#138a9a;
  --ink:#3a3f45;
  --muted:#8c949b;
  --line:#dde3e8;
  --pale:#f3f7fb;
  --white:#ffffff;
  --green:#4cb86a;
  --blue:#2b8fd9;
  --orange:#f7941d;
  --red:#f15a24;
  --hero-green:#3be23b;
  --footer:#2b2f36;
  --footer-line:#3d424a;
}
*{box-sizing:border-box;margin:0;padding:0}
html,body{width:1200px;height:3114px;overflow:hidden}
body{font-family:"Barlow",Arial,sans-serif;color:var(--ink);background:var(--white);position:relative}
a{color:inherit;text-decoration:none}
.abs{position:absolute}

/* header */
.site-header{position:absolute;top:0;left:0;width:1200px;height:58px;background:var(--white)}
.brand{position:absolute;left:112px;top:13px;display:flex;align-items:center;gap:8px;font-size:27px;font-weight:500;color:var(--teal);letter-spacing:-.3px}
.brand-dot{width:30px;height:30px;border-radius:50%;background:var(--teal)}
.main-nav a{position:absolute;top:20px;font-size:14px;font-weight:500;letter-spacing:2px;color:#4a5058}
.search-icon{position:absolute;left:928px;top:18px}
.btn-signin{position:absolute;left:978px;top:8px;width:110px;height:38px;background:var(--teal);color:#fff;font-size:13px;font-weight:600;letter-spacing:2px;display:flex;align-items:center;justify-content:center}

/* hero */
.hero{position:absolute;top:58px;left:0;width:1200px;height:554px;background:linear-gradient(100deg,#1a1f3c 0%,#2a2e62 30%,#3c2a6a 48%,#1d4a8e 62%,#3a5ea8 80%,#27315a 100%)}
.hero-copy{position:absolute;left:112px;top:145px;color:#fff}
.welcome{width:220px;border-top:1px solid #fff;border-bottom:1px solid #fff;padding:4px 0;text-align:center;font-size:17px;letter-spacing:18px;font-weight:400}
.hero-title{margin-top:20px;font-size:45px;font-weight:300;letter-spacing:5px;line-height:50px}
.hero-title strong{display:block;color:var(--hero-green);font-weight:600;letter-spacing:5px}
.hero-actions{margin-top:25px;display:flex;gap:17px}
.btn-outline{height:41px;border:2px solid #fff;color:#fff;font-size:13px;letter-spacing:2.5px;display:flex;align-items:center;justify-content:center}
.btn-teal{height:41px;background:var(--teal);border:2px solid #fff;color:#fff;font-size:13px;letter-spacing:2.5px;display:flex;align-items:center;justify-content:center}

/* section titles */
.section-title{position:absolute;left:0;width:1200px;text-align:center;font-size:34px;font-weight:300;letter-spacing:4px;color:var(--teal)}

/* programs */
.programs{position:absolute;top:612px;left:0;width:1200px;height:498px;background:var(--pale)}
.program-card{position:absolute;top:135px;width:218px;height:293px;background:#fff;border:1px solid var(--line)}
.program-head{height:85px;color:#fff;text-align:center;padding-top:18px}
.program-head small{display:block;font-size:11px;letter-spacing:2px;padding-bottom:6px;margin:0 60px;border-bottom:1px dotted rgba(255,255,255,.7)}
.program-head h3{margin-top:8px;font-size:16px;font-weight:600;letter-spacing:2px}
.program-list li{list-style:none;height:33px;line-height:33px;border-bottom:1px solid #edf0f3;text-align:center;font-size:12px;letter-spacing:1.5px;color:#7c848b}
.program-more{text-align:center;font-size:14px;letter-spacing:12px;color:#7c848b;margin-top:22px}
.program-btn{position:absolute;left:13px;right:13px;bottom:17px;height:34px;background:var(--teal);color:#fff;font-size:12px;font-weight:500;letter-spacing:.5px;display:flex;align-items:center;justify-content:center}

/* features */
.features{position:absolute;top:1110px;left:0;width:1200px;height:536px;background:#fff}
.feature-box{position:absolute;top:125px;width:278px;height:243px;border:1px solid var(--line);text-align:center;padding-top:75px}
.feature-icon{position:absolute;top:73px;width:104px;height:100px;border-radius:8px}
.feature-box h3{font-size:15px;font-weight:400;letter-spacing:.5px;color:#3a3f45}
.feature-box p{margin:18px auto 0;width:220px;font-size:12.5px;line-height:18px;color:#9aa1a8}
.btn-small{position:absolute;left:80px;width:116px;height:36px;bottom:32px;border:1px solid var(--teal);color:var(--teal);font-size:11.5px;letter-spacing:1px;display:flex;align-items:center;justify-content:center}
.btn-catalog{position:absolute;left:475px;top:422px;width:250px;height:42px;background:var(--teal);color:#fff;font-size:13px;letter-spacing:3px;display:flex;align-items:center;justify-content:center}

/* blogs */
.blogs{position:absolute;top:1646px;left:0;width:1200px;height:513px;background:var(--pale)}
.blog-card{position:absolute;top:135px;width:305px;height:316px}
.blog-image{height:166px}
.blog-body{position:absolute;left:12px;right:12px;top:139px;height:177px;background:#fff;padding:22px 22px 0}
.blog-meta{display:flex;justify-content:space-between;font-size:11px;color:#9aa1a8;letter-spacing:.5px}
.blog-meta .date{color:var(--teal)}
.blog-body h3{margin-top:8px;font-size:15px;font-weight:400;line-height:18px;color:#3a3f45}
.blog-body p{margin-top:8px;font-size:12.5px;line-height:16px;color:#9aa1a8}
.read-more{display:inline-block;margin-top:10px;font-size:11.5px;color:var(--teal);letter-spacing:.5px;border-bottom:1px solid var(--teal);padding-bottom:3px}

/* documents */
.documents{position:absolute;top:2159px;left:0;width:1200px;height:639px;background:#fff}
.doc-card{position:absolute;top:160px;width:471px;height:170px;background:var(--pale);padding:24px 20px 0 118px}
.doc-avatar{position:absolute;left:24px;top:57px;width:72px;height:72px;border-radius:50%}
.doc-time{display:flex;align-items:center;gap:6px;font-size:12px;color:var(--teal)}
.doc-card h3{margin-top:10px;font-size:17px;font-weight:400;color:#3a3f45}
.doc-card p{margin-top:6px;font-size:13px;line-height:18px;color:#8c949b}
.slider-arrow{position:absolute;top:228px;width:36px;height:36px;background:#8fd3dc;display:flex;align-items:center;justify-content:center}
.about-text{position:absolute;left:240px;top:506px;width:720px;text-align:center;font-size:14px;line-height:22px;color:#8c949b;letter-spacing:.3px}

/* footer */
.site-footer{position:absolute;top:2798px;left:0;width:1200px;height:316px;background:var(--footer);color:#fff}
.footer-rule{position:absolute;left:112px;width:1000px;height:1px;background:var(--footer-line)}
.footer-head{position:absolute;top:82px;font-size:15px;letter-spacing:2px;font-weight:400}
.footer-links{position:absolute;top:120px;list-style:none}
.footer-links li{font-size:12px;line-height:23px;color:#e4e7ea}
.lang-select{position:absolute;left:112px;top:256px;width:144px;height:36px;border-radius:18px;background:#3f444c;font-size:13px;display:flex;align-items:center;padding:0 0 0 24px;gap:50px}
.copyright{position:absolute;left:474px;top:267px;font-size:11.5px;color:#d5d9dd}
.follow{position:absolute;left:848px;top:267px;font-size:11.5px;color:#d5d9dd}
.social{position:absolute;top:259px;width:28px;height:28px}
</style>
</head>
<body>

<header class="site-header">
  <a class="brand" href="#"><span class="brand-dot"></span>Gridwell Review</a>
  <nav class="main-nav">
    <a href="#" style="left:426px">BROWSE</a>
    <a href="#" style="left:521px">SEARCH</a>
    <a href="#" style="left:617px">ADD</a>
    <a href="#" style="left:680px">CONTACT US</a>
  </nav>
  <svg class="search-icon" width="20" height="20" viewBox="0 0 20 20" aria-label="Search"><circle cx="8" cy="8" r="6" fill="none" stroke="#1aa3b5" stroke-width="2"/><line x1="12.5" y1="12.5" x2="18" y2="18" stroke="#1aa3b5" stroke-width="2"/></svg>
  <a class="btn-signin" href="#">SIGN IN</a>
</header>

<section class="hero" role="img" aria-label="Technician working at a laptop between glowing server racks in a data centre">
  <div class="hero-copy">
    <div class="welcome">WELCOME</div>
    <h1 class="hero-title">YOUR DEFINITIVE<br>GUIDE TO<strong>TECHNOLOGY AUDIT</strong></h1>
    <div class="hero-actions">
      <a class="btn-outline" href="#" style="width:222px">AUDITS PROGRAMS</a>
      <a class="btn-teal" href="#" style="width:127px">SEARCH</a>
    </div>
  </div>
</section>

<section class="programs">
  <h2 class="section-title" style="top:56px">FIND YOUR AUDIT PROGRAM</h2>

  <article class="program-card" style="left:112px">
    <div class="program-head" style="background:var(--green)"><small>VIEW BY</small><h3>TECHNOLOGY TYPE</h3></div>
    <ul class="program-list"><li>MAINFRAME</li><li>DATABASE</li><li>NETWORK</li></ul>
    <div class="program-more">MORE</div>
    <a class="program-btn" href="#">GET STARTED</a>
  </article>
  <article class="program-card" style="left:365px">
    <div class="program-head" style="background:var(--blue)"><small>VIEW BY</small><h3>RISK DESCRIPTION</h3></div>
    <ul class="program-list"><li>ATTACK</li><li>DATA LOSS</li><li>SERVICE OUTAGE</li></ul>
    <div class="program-more">MORE</div>
    <a class="program-btn" href="#">GET STARTED</a>
  </article>
  <article class="program-card" style="left:617px">
    <div class="program-head" style="background:var(--orange)"><small>VIEW BY</small><h3>CONTROL DESCRIPTION</h3></div>
    <ul class="program-list"><li>PENETRATION TEST</li><li>BACKUP DATA</li><li>&nbsp;</li></ul>
    <div class="program-more">MORE</div>
    <a class="program-btn" href="#">GET STARTED</a>
  </article>
  <article class="program-card" style="left:868px">
    <div class="program-head" style="background:var(--red)"><small>VIEW BY</small><h3>AUDIT TYPE</h3></div>
    <ul class="program-list"><li>ITGC</li><li>SO X</li><li>SAS 70</li></ul>
    <div class="program-more">MORE</div>
    <a class="program-btn" href="#">GET STARTED</a>
  </article>
</section>

<section class="features">
  <div class="feature-icon" role="img" aria-label="Icon of stacked audit documents" style="left:199px;background:linear-gradient(160deg,#2aa0e6,#0f5fb0)"></div>
  <div class="feature-icon" role="img" aria-label="Icon of a microchip" style="left:548px;background:linear-gradient(160deg,#ffb52a,#f07a12)"></div>
  <div class="feature-icon" role="img" aria-label="Icon of tools in front of a server" style="left:895px;background:linear-gradient(160deg,#2aa0e6,#0f5fb0)"></div>

  <article class="feature-box" style="left:112px">
    <h3>SEARCH FOR AUDIT TESTS</h3>
    <p>Search the full range of Technology audit tests in the Catalog.</p>
    <a class="btn-small" href="#">VIEW MORE</a>
  </article>
  <article class="feature-box" style="left:461px">
    <h3>BROWSE CALOG AUDIT TESTS</h3>
    <p>A range of popular Technology Audit Tests for use in auditing various technologies.</p>
    <a class="btn-small" href="#">VIEW MORE</a>
  </article>
  <article class="feature-box" style="left:808px">
    <h3>ADDITIONAL AUDITOR RESOURCES</h3>
    <p>Audit Templates, Frameworks and Links to other useful sites.</p>
    <a class="btn-small" href="#">VIEW MORE</a>
  </article>
  <a class="btn-catalog" href="#">AUDIT TEST TO CATALOG</a>
</section>

<section class="blogs">
  <h2 class="section-title" style="top:58px">LATEST BLOGS</h2>

  <article class="blog-card" style="left:114px">
    <div class="blog-image" role="img" aria-label="Person browsing a website on a laptop beside a coffee cup" style="background:linear-gradient(135deg,#5a4032,#2b2622 55%,#8a6b55)"></div>
    <div class="blog-body">
      <div class="blog-meta"><span>BY ADMIN</span><span class="date">17 JULY 2015</span></div>
      <h3>4 Springtime Color Schemes to Try at Home</h3>
      <p>Harrowfield Construction LTD is a London based developer and contractor...</p>
      <a class="read-more" href="#">READ MORE</a>
    </div>
  </article>
  <article class="blog-card" style="left:448px">
    <div class="blog-image" role="img" aria-label="Business team meeting in front of a screen showing a bar chart" style="background:linear-gradient(135deg,#c9d6e2,#6f8fb3 50%,#2e3a4c)"></div>
    <div class="blog-body">
      <div class="blog-meta"><span>BY ADMIN</span><span class="date">17 JULY 2015</span></div>
      <h3>4 Springtime Color Schemes to Try at Home</h3>
      <p>Harrowfield Construction LTD is a London based developer and contractor...</p>
      <a class="read-more" href="#">READ MORE</a>
    </div>
  </article>
  <article class="blog-card" style="left:781px">
    <div class="blog-image" role="img" aria-label="Woman working on a laptop at a wooden café counter" style="background:linear-gradient(135deg,#4a2f22,#9a6a4a 50%,#d8b08a)"></div>
    <div class="blog-body">
      <div class="blog-meta"><span>BY ADMIN</span><span class="date">17 JULY 2015</span></div>
      <h3>4 Springtime Color Schemes to Try at Home</h3>
      <p>Harrowfield Construction LTD is a London based developer and contractor...</p>
      <a class="read-more" href="#">READ MORE</a>
    </div>
  </article>
</section>

<section class="documents">
  <h2 class="section-title" style="top:72px">POPULAR DOCUMENT</h2>

  <a class="slider-arrow" href="#" style="left:50px" aria-label="Previous"><svg width="16" height="16" viewBox="0 0 16 16"><path d="M14 8H3M7 3L2 8l5 5" fill="none" stroke="#fff" stroke-width="2"/></svg></a>

  <article class="doc-card" style="left:112px">
    <div class="doc-avatar" role="img" aria-label="Author avatar" style="background:radial-gradient(circle at 50% 40%,#8a98a8,#2f3a48)"></div>
    <div class="doc-time"><svg width="12" height="12" viewBox="0 0 12 12"><circle cx="6" cy="6" r="5" fill="none" stroke="#1aa3b5"/><path d="M6 3v3h2" fill="none" stroke="#1aa3b5"/></svg>12 hours ago</div>
    <h3>Software Developer/Analyst - Web Developer</h3>
    <p>Harrowfield Construction LTD is a London based de-veloper and contractor Harrowfield Construction LTD is a London based developer....</p>
  </article>
  <article class="doc-card" style="left:617px">
    <div class="doc-avatar" role="img" aria-label="Author avatar" style="background:radial-gradient(circle at 50% 40%,#c9a27a,#5e4632)"></div>
    <div class="doc-time"><svg width="12" height="12" viewBox="0 0 12 12"><circle cx="6" cy="6" r="5" fill="none" stroke="#1aa3b5"/><path d="M6 3v3h2" fill="none" stroke="#1aa3b5"/></svg>12 hours ago</div>
    <h3>Software Developer/Analyst - Web Developer</h3>
    <p>Harrowfield Construction LTD is a London based de-veloper and contractor Harrowfield Construction LTD is a London based developer....</p>
  </article>

  <a class="slider-arrow" href="#" style="left:1113px" aria-label="Next"><svg width="16" height="16" viewBox="0 0 16 16"><path d="M2 8h11M9 3l5 5-5 5" fill="none" stroke="#fff" stroke-width="2"/></svg></a>

  <h2 class="section-title" style="top:392px">ABOUT US</h2>
  <p class="about-text">This is Layoutwerk's version of Lorem Ipsum. Proin gravida nibh vel velit auctor aliquet. Aenean sollicitudin, lorem quis bibendum auctor, nisi elit consequat ipsum, nec sagittis sem nibh id elit. Duis sed odio sit amet nibh vulputate cursus a sit amet mauris.</p>
</section>

<footer class="site-footer">
  <div class="footer-rule" style="top:32px"></div>

  <h4 class="footer-head" style="left:112px">CORPORATE</h4>
  <ul class="footer-links" style="left:112px"><li>Home</li><li>About Us</li><li>Jobs</li></ul>
  <ul class="footer-links" style="left:232px"><li>Contact Us</li><li>Nestly Blog</li><li>Sitemap</li></ul>

  <h4 class="footer-head" style="left:394px">STUDENTS</h4>
  <ul class="footer-links" style="left:394px"><li>How It Works</li><li>Post a Sublet</li><li>Register</li></ul>
  <ul class="footer-links" style="left:536px"><li>Write For Us</li><li>Review Guidelines and Tips</li><li>Current markets</li></ul>

  <h4 class="footer-head" style="left:789px">LANDLORDS</h4>
  <ul class="footer-links" style="left:789px"><li>How It Works</li><li>Register</li></ul>

  <h4 class="footer-head" style="left:984px">LEGAL</h4>
  <ul class="footer-links" style="left:984px"><li>Terms of Use</li><li>Privacy Policy</li><li>Disclaimer</li></ul>

  <div class="footer-rule" style="top:229px"></div>

  <div class="lang-select">English <svg width="12" height="8" viewBox="0 0 12 8"><path d="M1 1l5 6 5-6z" fill="#fff"/></svg></div>
  <p class="copyright">Copyright © 2015 Gridwell Review. Powered by Storelane.</p>
  <p class="follow">Follow us on</p>
  <span class="social" style="left:947px;background:#3b5fa8"></span>
  <span class="social" style="left:982px;background:#e0468a"></span>
  <span class="social" style="left:1016px;background:#3fb0e6"></span>
  <span class="social" style="left:1051px;background:#4a7fb0"></span>
</footer>

</body>
</html>
```